Real Estate Development Company Stationary

We need our company, business card, letterhead, pocket folder and envelope designed.

We are a new real estate development company. We focus on data centre, commercial and real estate development.

Please see attached for our logo. Since it's a new logo, you still can make minor adjust if you like it makes senses

The client has sent me a business card he really likes. Please see file 3.

Target Market(s)

Real Estate Investors
Large corporations
Home buyers

Industry/Entity Type

Real Estate

```html
<!DOCTYPE html>
<html lang="en">
<head>
<meta charset="utf-8">
<title>Vantor Development Inc. – Business Card</title>
<link rel="stylesheet" href="https://fonts.googleapis.com/css2?family=Open+Sans:wght@400;600;700&display=swap">
<style>
  :root {
    --page-bg: #e9e6e1;
    --card-white: #ffffff;
    --brand-green: #6abf45;
    --brand-navy: #1f4e8f;
    --ink-grey: #4a4a4a;
    --card-blue-light: #2a5c9e;
    --card-blue-dark: #0c2f66;
    --card-shadow: rgba(0, 0, 0, 0.22);
  }
  * { box-sizing: border-box; margin: 0; padding: 0; }
  html, body {
    width: 1200px;
    height: 1024px;
    overflow: hidden;
    background: var(--page-bg);
    font-family: "Open Sans", Arial, sans-serif;
  }
  .canvas {
    position: relative;
    width: 1200px;
    height: 1024px;
  }
  .card {
    position: absolute;
    width: 700px;
    height: 400px;
    border-radius: 4px;
    box-shadow: 0 14px 30px var(--card-shadow);
  }

  /* Front of card */
  .card-front {
    left: 100px;
    top: 90px;
    background: var(--card-white);
  }
  .brand-block {
    position: absolute;
    right: 48px;
    top: 52px;
    display: flex;
    align-items: center;
    gap: 12px;
  }
  .brand-dot {
    width: 22px;
    height: 22px;
    border-radius: 50%;
    background: var(--brand-green);
  }
  .brand-name {
    font-weight: 700;
    font-size: 30px;
    color: var(--brand-navy);
    letter-spacing: 0.2px;
  }
  .contact-block {
    position: absolute;
    right: 48px;
    top: 118px;
    text-align: right;
    font-size: 15px;
    color: var(--ink-grey);
    line-height: 1.7;
  }
  .contact-line {
    display: flex;
    justify-content: flex-end;
    align-items: center;
    gap: 6px;
  }
  .contact-line + .contact-line { margin-top: 1px; }
  .icon {
    width: 14px;
    height: 14px;
    flex: none;
  }
  .spacer { width: 10px; }
  .person {
    position: absolute;
    left: 48px;
    top: 220px;
    display: flex;
    align-items: baseline;
    gap: 8px;
  }
  .person-name {
    font-weight: 700;
    font-size: 30px;
    color: var(--brand-green);
  }
  .person-title {
    font-weight: 600;
    font-size: 19px;
    color: var(--brand-navy);
  }
  .email-line {
    position: absolute;
    left: 48px;
    bottom: 40px;
    display: flex;
    align-items: center;
    gap: 8px;
    font-size: 15px;
    color: var(--ink-grey);
  }

  /* Back of card */
  .card-back {
    left: 400px;
    top: 534px;
    background: radial-gradient(circle at 40% 30%, var(--card-blue-light) 0%, var(--card-blue-dark) 75%);
  }
  .back-brand {
    position: absolute;
    left: 0;
    right: 0;
    top: 170px;
    display: flex;
    justify-content: center;
    align-items: center;
    gap: 14px;
  }
  .back-brand .brand-dot {
    width: 30px;
    height: 30px;
  }
  .back-brand .brand-name {
    color: var(--card-white);
    font-size: 36px;
  }
  .back-web {
    position: absolute;
    left: 48px;
    bottom: 40px;
    font-size: 16px;
    color: var(--card-white);
  }
  .back-web .web-accent { color: var(--brand-green); }
</style>
</head>
<body>
<main class="canvas">

  <section class="card card-front" aria-label="Business card front">
    <div class="brand-block">
      <span class="brand-dot"></span>
      <span class="brand-name">Vantor Development Inc.</span>
    </div>

    <div class="contact-block">
      <div class="contact-line">48 Harbor Line Road, Ashford SC 29510</div>
      <div class="contact-line">
        <svg class="icon" viewBox="0 0 14 14" aria-hidden="true"><path fill="#6abf45" d="M3 1h3l1 3-2 1.5a7 7 0 0 0 3.5 3.5L10 7l3 1v3a2 2 0 0 1-2 2C5.5 13 1 8.5 1 3a2 2 0 0 1 2-2z"/></svg>
        <span>555 214 3307</span>
        <span class="spacer"></span>
        <svg class="icon" viewBox="0 0 14 14" aria-hidden="true"><rect x="3.5" y="1" width="7" height="12" rx="1.4" fill="#6abf45"/><rect x="5" y="2.6" width="4" height="7" fill="#fff"/></svg>
        <span>555 618 4492</span>
      </div>
      <div class="contact-line">
        <svg class="icon" viewBox="0 0 14 14" aria-hidden="true"><circle cx="7" cy="7" r="6" fill="#6abf45"/><path d="M1 7h12M7 1c-2.5 3-2.5 9 0 12M7 1c2.5 3 2.5 9 0 12" stroke="#fff" stroke-width="1" fill="none"/></svg>
        <span>www.vantordev.ca</span>
      </div>
    </div>

    <div class="person">
      <span class="person-name">Mara Linwood,</span>
      <span class="person-title">Project Manager</span>
    </div>

    <div class="email-line">
      <svg class="icon" viewBox="0 0 14 14" aria-hidden="true"><rect x="0.5" y="2.5" width="13" height="9" fill="#6abf45"/><path d="M1 3l6 5 6-5" stroke="#fff" stroke-width="1.2" fill="none"/></svg>
      <span>mara.linwood@vantordev.ca</span>
    </div>
  </section>

  <section class="card card-back" aria-label="Business card back">
    <div class="back-brand">
      <span class="brand-dot"></span>
      <span class="brand-name">Vantor Development Inc.</span>
    </div>
    <div class="back-web">www.<span class="web-accent">vantordev</span>.ca</div>
  </section>

</main>
</body>
</html>
```